Private London College Prospectus

A single spread to begin with followed by treatments for a couple of awkward spreads in the brochure. Attached docs include previous few years to show how the design has evolved. We're now looking for a different direction
Outline: Private college in Central London.
Mainly A-levels but also GCSE courses
Consistently at the top of London results table
Operated by the owners
Prospectus is sent to anyone enquiring about the college

Target Market(s)

High net worth families in the Uk and abroad

Industry/Entity Type

College

Requirements
Must have
• Modern fonts
• House colour is purple - PMS 8804
• Teacher quote
• Page quote
Nice to have
• See attachments - the gryphon is part of their logo but not essential
Should not have
• Shouldn't be too fussy or cluttered
• No script fonts (probably) no italics in main text

```html
<!DOCTYPE html>
<html lang="en">
<head>
<meta charset="utf-8">
<title>Halworth Prospectus – The Halworth Ethos</title>
<link rel="stylesheet" href="https://fonts.googleapis.com/css2?family=Libre+Baskerville:ital@0;1&family=Montserrat:wght@400;500;600;700&display=swap">
<style>
  :root {
    --house-purple: #4f3a73;
    --ink-purple: #48336e;
    --page: #f5f5f8;
    --page-shade: #e6e6ec;
    --body-ink: #4a4560;
    --rule: #6a5890;
  }
  * { margin: 0; padding: 0; box-sizing: border-box; }
  html, body { width: 1200px; height: 889px; overflow: hidden; }
  body {
    background: var(--house-purple);
    font-family: "Montserrat", sans-serif;
    position: relative;
  }
  .spread {
    position: absolute;
    left: 60px; top: 95px;
    width: 1080px; height: 700px;
    display: flex;
    box-shadow: 0 18px 40px rgba(20, 10, 40, .35);
  }
  .page {
    position: relative;
    width: 540px; height: 700px;
    background: var(--page);
  }
  .page--left { background: linear-gradient(to right, var(--page) 88%, var(--page-shade)); }
  .page--right { background: linear-gradient(to left, var(--page) 88%, var(--page-shade)); }
  .folio {
    position: absolute; top: 26px;
    font-size: 8px; font-weight: 600; color: var(--ink-purple);
  }
  .page--left .folio { left: 28px; }
  .page--right .folio { right: 28px; }
  .web {
    position: absolute; bottom: 26px;
    font-family: "Libre Baskerville", serif; font-style: italic;
    font-size: 8px; color: var(--ink-purple);
  }
  .page--left .web { left: 200px; }
  .page--right .web { left: 220px; }

  .ethos-title {
    position: absolute; left: 80px; top: 120px;
    font-weight: 400; font-size: 17px; color: var(--ink-purple);
    letter-spacing: .2px;
  }
  .ethos-intro {
    position: absolute; left: 80px; top: 150px; width: 270px;
    font-size: 8px; line-height: 1.45; color: var(--body-ink);
  }
  .ethos-rule {
    position: absolute; left: 80px; top: 210px;
    width: 50px; height: 1px; background: var(--rule);
  }
  .ethos-body {
    position: absolute; left: 80px; top: 225px; width: 190px;
    font-size: 6.6px; line-height: 1.42; color: var(--body-ink);
  }
  .ethos-body h3 {
    font-size: 6.8px; font-weight: 700; color: var(--ink-purple);
    margin: 0 0 5px;
  }
  .ethos-body p { margin-bottom: 6px; }

  .photo {
    position: absolute;
  }
  .photo--classroom {
    left: 300px; top: 300px; width: 375px; height: 270px;
    background: linear-gradient(135deg, #d8c7a6 0%, #b89872 45%, #6f5a4c 80%, #3e3440 100%);
  }
  .photo--study {
    left: 688px; top: 340px; width: 262px; height: 290px;
    background: linear-gradient(160deg, #cdbfa8 0%, #a88366 40%, #7a4a3e 70%, #3f3036 100%);
  }

  .page-quote {
    position: absolute; left: 80px; top: 180px; width: 260px;
    font-family: "Libre Baskerville", serif; font-weight: 400;
    font-size: 27px; line-height: 1.08; color: var(--ink-purple);
  }
  .teacher {
    position: absolute; left: 405px; top: 185px; width: 110px;
  }
  .teacher__portrait {
    width: 104px; height: 96px;
    background: linear-gradient(180deg, #e9e9ee, #c9c6cf);
  }
  .teacher__name {
    margin-top: 8px;
    font-size: 8px; font-weight: 700; color: #2d2740;
  }
  .teacher__role {
    font-size: 7.5px; font-weight: 600; color: var(--ink-purple);
  }
  .teacher__quote {
    margin-top: 5px; padding-left: 6px;
    border-left: 1px solid var(--rule);
    font-size: 7.2px; line-height: 1.4; color: var(--body-ink);
  }
</style>
</head>
<body>
  <main class="spread">
    <section class="page page--left">
      <span class="folio">06</span>
      <h1 class="ethos-title">The Halworth Ethos</h1>
      <p class="ethos-intro">Based in the heart of Mayfair in central London, Halworth is a top performing independent sixth-form college, offering a broad A-level and GCSE curriculum for students from public, state and private school backgrounds.</p>
      <div class="ethos-rule"></div>
      <div class="ethos-body">
        <h3>Why Choose Halworth?</h3>
        <p>The majority of students who come to Halworth do so because of our reputation for excellent A-level and GCSE results. This is true of students both on our full two-year programme, as well as those on the one-year intensive programme. Most students will progress on to a top 20 UK university.</p>
        <p>Students are taught very much by traditional methods, in small groups, concentrating on the skills needed to pass examinations and to be successful at university. All teachers at Halworth are subject specialists and most have experience as examiners. They are particularly successful with young people: they are able to motivate and communicate with them in ways which they understand. Barriers are quickly broken down, enhancing the learning process.</p>
        <h3>How Do We Get The Best Out Of Our Students?</h3>
        <p>Students benefit from individually tailored attention outside of classes – a key element of our successful A-level and GCSE programmes. At Halworth each student has a Curriculum Manager and a Personal Tutor, who provide advice on study skills, subject choices and careers, and who also monitor progress in regular meetings with students.</p>
        <p>We expect full commitment from our students and as such we have strict rules on attendance and timely submission of assignments. Parents are able to monitor progress through monthly reports, easily accessible using our online reporting system. Parents' Evenings are held during the Autumn and Spring terms.</p>
        <p>We encourage our students every step of the way and we help them to build confidence through examination success. We see the learning process as a successful partnership between students, tutors and parents.</p>
      </div>
      <span class="web">www.halworthcollege.co.uk</span>
    </section>

    <section class="page page--right">
      <span class="folio">07</span>
      <h2 class="page-quote">A modern college with a traditional approach</h2>
      <aside class="teacher">
        <div class="teacher__portrait" role="img" aria-label="Portrait photograph of the Head of Economics"></div>
        <p class="teacher__name">Rajan Mehta</p>
        <p class="teacher__role">Head of Economics</p>
        <p class="teacher__quote">We teach students how to develop their powers of analysis and independence of thought - crucial to success at university and beyond.</p>
      </aside>
      <span class="web">www.halworthcollege.co.uk</span>
    </section>

    <div class="photo photo--classroom" role="img" aria-label="Photograph of a small seminar class seated around a U-shaped table with a teacher standing by the wall"></div>
    <div class="photo photo--study" role="img" aria-label="Photograph of a student writing at a desk in a library classroom"></div>
  </main>
</body>
</html>
```